Professional law firm looking for new professional and eye-catching business card design

Law firm in need of new business card design using existing firm logo and firm colors on thick card stock. Firm colors are navy blue, cyan blue, and gray. Please use firm's logo either on the back of the card or on the front and back. I am looking for something eye-catching and resonating but also professional.

Target Market(s)

Law firm growth by attracting clients with professional, creative, and attractive business cards.

Industry/Entity Type

Legal/Law Firm

Contact Information for Business Card

Name: Derek T. Halloway, Esq., Address: 517 E. Quintley Blvd., P.O. Box 641, Tavares, FL 32790, Phone numbers: (352) 555-0187 Office, (352) 555-0142 Fax, email address: DerekH@hqlegalfx.com, website: www.HQLegalFX.com

Font styles to use
Other font styles liked:
• Font as close as possible to matching law firm logo.

Requirements
Must have
• Must have business card details and law firm logo with law firm colors.

```html
<!DOCTYPE html>
<html lang="en">
<head>
<meta charset="utf-8">
<title>Halloway + Quintley, P.A. — Business Card</title>
<link href="https://fonts.googleapis.com/css2?family=Inter:wght@400;700&display=swap" rel="stylesheet">
<style>
  :root {
    --page: #f2f3f5;
    --navy: #181d2a;
    --cyan: #1ea0dc;
    --gray: #b2b1b6;
    --silver: #8f9097;
    --ink: #1b202c;
  }
  * { margin: 0; padding: 0; box-sizing: border-box; }
  html, body {
    width: 1199px; height: 1200px; overflow: hidden;
    background: var(--page);
    font-family: "Inter", sans-serif;
  }
  .sheet {
    position: relative; width: 1199px; height: 1200px;
    display: flex; flex-direction: column; align-items: center;
    justify-content: center; gap: 48px;
  }
  .card {
    position: relative; width: 880px; height: 536px;
    box-shadow: 0 6px 14px rgba(0,0,0,0.28);
    overflow: hidden;
  }
  .card--front { background: var(--navy); }
  .card--back { background: var(--gray); }

  .justice-figure {
    position: absolute; left: 262px; top: 103px;
    width: 150px; height: 324px;
    background: linear-gradient(180deg, #9a9ba2 0%, var(--silver) 60%, #6f7078 100%);
    border-radius: 60px 60px 12px 12px;
    opacity: 0.9;
  }
  .firm-mark {
    position: absolute; left: 428px; top: 258px;
    color: var(--cyan); font-weight: 700;
  }
  .firm-mark__name { font-size: 52px; letter-spacing: 2px; line-height: 1; }
  .firm-mark__rule { height: 2px; background: var(--cyan); width: 226px; margin: 10px 0 8px; }
  .firm-mark__sub { font-size: 15px; letter-spacing: 0.5px; }

  .corner-block {
    position: absolute; right: 0; top: 0;
    width: 203px; height: 233px; background: var(--navy);
  }
  .corner-block .justice-figure {
    left: 40px; top: 48px; width: 40px; height: 130px; border-radius: 20px 20px 4px 4px;
  }
  .corner-block .firm-mark { left: 86px; top: 106px; }
  .corner-block .firm-mark__name { font-size: 20px; letter-spacing: 1px; }
  .corner-block .firm-mark__rule { width: 92px; height: 1px; margin: 4px 0 3px; }
  .corner-block .firm-mark__sub { font-size: 6.5px; letter-spacing: 0; }

  .identity { position: absolute; left: 51px; top: 222px; color: var(--ink); }
  .identity__name { font-size: 35px; font-weight: 700; letter-spacing: 0.3px; text-transform: uppercase; line-height: 1; }
  .identity__title { font-size: 22px; font-weight: 400; margin-top: 6px; text-transform: uppercase; }

  .contact-list { position: absolute; left: 51px; top: 337px; list-style: none; color: var(--ink); }
  .contact-list li {
    display: flex; align-items: center; gap: 15px;
    font-size: 23px; height: 39.5px;
  }
  .contact-list svg { width: 24px; height: 24px; flex: none; }
</style>
</head>
<body>
<main class="sheet">
  <section class="card card--front" aria-label="Card front">
    <div class="justice-figure" role="img" aria-label="Illustration of Lady Justice holding scales and a sword"></div>
    <div class="firm-mark">
      <div class="firm-mark__name">HQ LAW</div>
      <div class="firm-mark__rule"></div>
      <div class="firm-mark__sub">Halloway + Quintley, P.A.</div>
    </div>
  </section>

  <section class="card card--back" aria-label="Card back">
    <div class="corner-block">
      <div class="justice-figure" role="img" aria-label="Small illustration of Lady Justice"></div>
      <div class="firm-mark">
        <div class="firm-mark__name">HQ LAW</div>
        <div class="firm-mark__rule"></div>
        <div class="firm-mark__sub">Halloway + Quintley, P.A.</div>
      </div>
    </div>

    <div class="identity">
      <div class="identity__name">Derek T. Halloway, Esq.</div>
      <div class="identity__title">Lawyer</div>
    </div>

    <ul class="contact-list">
      <li>
        <svg viewBox="0 0 24 24"><circle cx="12" cy="12" r="11" fill="var(--navy)"/><path d="M12 5.5a4 4 0 0 0-4 4c0 3 4 8 4 8s4-5 4-8a4 4 0 0 0-4-4z" fill="var(--gray)"/><circle cx="12" cy="9.5" r="1.5" fill="var(--navy)"/></svg>
        517 E. Quintley Blvd., P.O. Box 641, Tavares, FL 32790
      </li>
      <li>
        <svg viewBox="0 0 24 24"><circle cx="12" cy="12" r="11" fill="var(--navy)"/><path d="M8.5 6.5l2 2.2-1.2 1.6c.8 1.7 2 2.9 3.6 3.7l1.6-1.2 2.2 2-1 1.9c-4.2-.4-7.5-3.7-7.9-7.9z" fill="var(--gray)"/></svg>
        (352) 555-0187 Office, (352) 555-0142 Fax
      </li>
      <li>
        <svg viewBox="0 0 24 24"><circle cx="12" cy="12" r="11" fill="var(--navy)"/><rect x="6.5" y="8" width="11" height="8" rx="1" fill="none" stroke="var(--gray)" stroke-width="1.4"/><path d="M6.8 8.5L12 12.5l5.2-4" fill="none" stroke="var(--gray)" stroke-width="1.4"/></svg>
        DerekH@hqlegalfx.com
      </li>
      <li>
        <svg viewBox="0 0 24 24"><circle cx="12" cy="12" r="11" fill="var(--navy)"/><g fill="none" stroke="var(--gray)" stroke-width="1.2"><circle cx="12" cy="12" r="6"/><ellipse cx="12" cy="12" rx="2.6" ry="6"/><path d="M6 12h12"/></g></svg>
        www.HQLegalFX.com
      </li>
    </ul>
  </section>
</main>
</body>
</html>
```